This is for a poster that will be hanging in the window of a Men's Suit Store in the mall:
Size 4 feet wide by 6 feet high
Main point is: A sale on "Suits" or "Men's Suits" at 40%-60% off ( the 40%-60% off should be the focal point)
Some words that can be used are "Sale" or "Clearance Sale"
Some key words that can be used to make it urgent are "limited time offer" or something similar.
You can get creative, the point is for the customer to want to come into the store and buy a suit right away.
You may use a graphic (picture of a man in a suit). It is not necessary but if it looks good you can use it. (If you do use a picture, it should be of a modern fit or slim fit suit)
Sorry, the initial brief somehow got deleted from the project. Please see the updated brief.
Thanks
Reason: Project was closed for some reason, extended to give enough time to complete
Target Market(s)
Mostly Men ages 35-55
Industry/Entity Type
Store
Colors
Designer to choose colors to be used in the design.

```html
<!DOCTYPE html>
<html lang="en">
<head>
<meta charset="utf-8">
<title>Men's Suits Clearance Sale Poster</title>
<link rel="stylesheet" href="https://fonts.googleapis.com/css2?family=Archivo+Black&family=Jost:wght@400;600;700&display=swap">
<style>
  :root {
    --stage: #ececec;
    --blue-mid: #2b7fbd;
    --blue-deep: #0f4d8f;
    --blue-navy: #0b3c7a;
    --sale-red: #ec2a2d;
    --white: #ffffff;
    --wood-light: #d9a468;
    --wood-dark: #a8723f;
  }
  html, body {
    margin: 0;
    padding: 0;
    width: 1200px;
    height: 1200px;
    overflow: hidden;
    background: var(--stage);
  }
  .poster {
    position: absolute;
    left: 272px;
    top: 60px;
    width: 665px;
    height: 1080px;
    overflow: hidden;
    background:
      radial-gradient(circle at 50% 36%, rgba(92,192,236,0.95) 0%, rgba(60,150,210,0.6) 28%, rgba(20,90,160,0) 62%),
      repeating-conic-gradient(from 0deg at 50% 36%, rgba(255,255,255,0.07) 0deg 9deg, rgba(255,255,255,0) 9deg 22deg),
      linear-gradient(180deg, var(--blue-mid) 0%, var(--blue-deep) 70%, var(--blue-navy) 100%);
    box-shadow: 0 6px 14px rgba(0,0,0,0.25);
    font-family: "Jost", "Futura", sans-serif;
    color: var(--white);
    text-align: center;
  }
  .line {
    position: absolute;
    left: 0;
    right: 0;
    margin: 0;
    line-height: 1;
    white-space: nowrap;
  }
  .store-name {
    top: 62px;
    font-size: 44px;
    font-weight: 600;
    letter-spacing: 2px;
  }
  .hanger-visual {
    position: absolute;
    left: 62px;
    top: 178px;
    width: 578px;
    height: 240px;
    background: linear-gradient(160deg, var(--wood-light), var(--wood-dark));
    clip-path: polygon(50% 0, 100% 80%, 100% 100%, 0 100%, 0 86%);
    opacity: 0.9;
  }
  .discount-tag {
    position: absolute;
    left: 83px;
    top: 412px;
    width: 497px;
    height: 318px;
    background: var(--sale-red);
    box-shadow: 0 4px 10px rgba(0,0,0,0.3);
    font-family: "Archivo Black", "Arial Black", sans-serif;
    font-size: 158px;
    letter-spacing: 3px;
  }
  .discount-tag .line { line-height: 1; }
  .discount-tag .first { top: 18px; }
  .discount-tag .second { top: 162px; }
  .headline { margin: 0; font-weight: 600; text-shadow: 2px 3px 0 rgba(0,0,0,0.35); }
  .headline-product { top: 756px; font-size: 58px; }
  .headline-sale { top: 818px; font-size: 63px; font-weight: 700; letter-spacing: 1px; }
  .urgency-top { top: 940px; font-size: 38px; font-weight: 700; }
  .urgency-main { top: 976px; font-size: 78px; font-weight: 700; }
  .urgency-rule {
    position: absolute;
    top: 1012px;
    height: 1px;
    width: 193px;
    background: rgba(255,255,255,0.8);
  }
  .urgency-rule.left { left: 0; }
  .urgency-rule.right { right: 0; }
</style>
</head>
<body>
  <main class="poster">
    <p class="line store-name">HARLOW MENSWEAR</p>

    <div class="hanger-visual" role="img" aria-label="Stack of wooden clothes hangers holding the sale tag"></div>

    <div class="discount-tag">
      <span class="line first">40%</span>
      <span class="line second">60%</span>
    </div>

    <h1 class="headline">
      <span class="line headline-product">Men's Suits</span>
      <span class="line headline-sale">CLEARANCE SALE</span>
    </h1>

    <div class="urgency-rule left"></div>
    <div class="urgency-rule right"></div>
    <p class="line urgency-top">LIMITED TIME</p>
    <p class="line urgency-main">OFFER</p>
  </main>
</body>
</html>
```